Corporate A3 Deskpad Design For Services Company

We need a design for a A3 desk pad for our clients with our information around the sides. Please find attached our logo, examples and other collateral that we have for inspiration.
Please see below for the details on what we want.
The colours are in both the A4 brochure design and the logo as well as our website www.brimwelltech.com.au.
Thanks,
RM
Target Market(s)
Corporate
Industry/Entity Type
It Company
Font styles to use
Sans Serif
Colors
Designer to choose colors to be used in the design.
Requirements
Must have
- We simply want a simple corporate design in our colours around the sides. The top left will have our contact information (name, phone, email, website etc). Underneath that will be filler text with 1 heading and text underneath. on the right will have 3 sections each with a heading.
Should not have
- Calendars

```html
<!DOCTYPE html>
<html lang="en">
<head>
<meta charset="utf-8">
<title>Brimwell Desk Pad</title>
<link rel="stylesheet" href="https://fonts.googleapis.com/css2?family=Arimo:ital,wght@0,400;0,700;1,700&display=swap">
<style>
  :root {
    --navy: #262a3a;
    --orange: #f05a22;
    --ink: #1c1c1c;
    --paper: #ffffff;
  }
  * { margin: 0; padding: 0; box-sizing: border-box; }
  html, body { width: 1200px; height: 949px; overflow: hidden; background: var(--paper); }
  body { font-family: "Arimo", Arial, sans-serif; color: var(--ink); }
  .deskpad { position: relative; width: 1200px; height: 949px; background: var(--paper); }

  .top-band { position: absolute; left: 0; top: 0; width: 100%; height: 92px; background: var(--navy); border-bottom: 6px solid var(--orange); }
  .contact { position: absolute; left: 68px; top: 18px; list-style: none; }
  .contact li { display: flex; align-items: center; gap: 8px; color: var(--orange); font-weight: 700; font-size: 14px; line-height: 21px; }
  .contact svg { width: 16px; height: 16px; flex: none; }

  .brand { position: absolute; left: 0; right: 0; top: 106px; text-align: center; }
  .brand-name { font-size: 48px; font-weight: 400; letter-spacing: 12px; color: var(--ink); line-height: 1; }

  .section h2 { font-size: 13px; font-weight: 700; font-style: italic; margin-bottom: 20px; }
  .section p { font-size: 10.5px; line-height: 16px; text-align: justify; }
  .section-left { position: absolute; left: 82px; top: 262px; width: 285px; }
  .section-right { position: absolute; left: 790px; width: 280px; }
  .section-right h2 { text-align: right; margin-bottom: 18px; }
  .section-right p { text-align-last: center; }
  .s1 { top: 186px; }
  .s2 { top: 296px; }
  .s3 { top: 406px; }

  .bottom-band { position: absolute; left: 0; bottom: 0; width: 100%; height: 80px; background: var(--navy); border-top: 6px solid var(--orange); display: flex; justify-content: center; align-items: center; }
  .bottom-band .brand-name { font-size: 26px; letter-spacing: 6px; color: var(--paper); }
</style>
</head>
<body>
<main class="deskpad">
  <header class="top-band">
    <ul class="contact">
      <li>
        <svg viewBox="0 0 24 24" aria-hidden="true"><path fill="#f05a22" d="M6.6 10.8a15.1 15.1 0 0 0 6.6 6.6l2.2-2.2c.3-.3.7-.4 1-.2 1.1.4 2.3.6 3.6.6.6 0 1 .4 1 1V20c0 .6-.4 1-1 1A17 17 0 0 1 3 4c0-.6.4-1 1-1h3.5c.6 0 1 .4 1 1 0 1.3.2 2.5.6 3.6.1.3 0 .7-.2 1z"/></svg>
        Telephone: 1300 555 014
      </li>
      <li>
        <svg viewBox="0 0 24 24" aria-hidden="true"><rect x="2" y="5" width="20" height="14" fill="#f05a22"/><path d="M2 5l10 8 10-8" fill="none" stroke="#262a3a" stroke-width="2"/></svg>
        Email: info@brimwelltech.com.au
      </li>
      <li>
        <svg viewBox="0 0 24 24" aria-hidden="true"><g fill="none" stroke="#f05a22" stroke-width="2"><circle cx="12" cy="12" r="9"/><ellipse cx="12" cy="12" rx="4" ry="9"/><path d="M3 12h18M5 7h14M5 17h14"/></g></svg>
        www.brimwelltech.com.au
      </li>
    </ul>
  </header>

  <div class="brand">
    <span class="brand-name">brimwell</span>
  </div>

  <section class="section section-left">
    <h2>Lorem Ipsum</h2>
    <p>Sed ut perspiciatis unde omnis iste natus error sit voluptatem accusantium doloremque laudantium, totam rem aperiam, eaque ipsa quae ab illo inventore veritatis et quasi architecto beatae vitae dicta sunt explicabo.</p>
  </section>

  <section class="section section-right s1">
    <h2>Lorem Ipsum</h2>
    <p>Sed ut perspiciatis unde omnis iste natus error sit voluptatem accusantium doloremque laudantium, totam rem aperiam, eaque ipsa quae ab illo inventore veritatis et quasi architecto beatae vitae dicta sunt explicabo.</p>
  </section>
  <section class="section section-right s2">
    <h2>Lorem Ipsum</h2>
    <p>Sed ut perspiciatis unde omnis iste natus error sit voluptatem accusantium doloremque laudantium, totam rem aperiam, eaque ipsa quae ab illo inventore veritatis et quasi architecto beatae vitae dicta sunt explicabo.</p>
  </section>
  <section class="section section-right s3">
    <h2>Lorem Ipsum</h2>
    <p>Sed ut perspiciatis unde omnis iste natus error sit voluptatem accusantium doloremque laudantium, totam rem aperiam, eaque ipsa quae ab illo inventore veritatis et quasi architecto beatae vitae dicta sunt explicabo.</p>
  </section>

  <footer class="bottom-band">
    <span class="brand-name">brimwell</span>
  </footer>
</main>
</body>
</html>
```